Profesional personal website needs design and business card

I need a business card with my professional name as a logo "Marlo Vitality" for my business. I am a Wellness Coach, consultant and trainer. So it should be professional, wellness oriented and modern.

Target Market(s)

Private clients, governments, corporations. Luxury and high market.

Industry/Entity Type

Health And Wellness

Contact Information for Business Card

Marlo Vitality should be the logo

Colors

Designer to choose colors to be used in the design.

Requirements
Must have
• Marlo Vitality
• Name: Tomás Arribal
• Wellness Coach, Consultant & Trainer.
• Website: www.marlovitality.example
• Phone:
• Spain (+34) 612 480 397
• (USA) +1 (555) 318 2046
Nice to have
• The most important is the design of "Marlo Vitality", as this is going to be my personal brand logo. It should be professional, wellness, high end and actual.
Should not have
• no golds, no baroque style..

```html
<!DOCTYPE html>
<html lang="en">
<head>
<meta charset="utf-8">
<title>Marlo Vitality — Business Card</title>
<link rel="stylesheet" href="https://fonts.googleapis.com/css2?family=Open+Sans:wght@400;700&display=swap">
<style>
  :root {
    --page-bg: #d9dadb;
    --card-dark: #2a2a2a;
    --card-light: #f6f6f6;
    --brand-blue: #4fb6d9;
    --text-grey: #555a5e;
    --rule-grey: #8a8d90;
    --on-dark: #f2f2f2;
  }
  * { box-sizing: border-box; margin: 0; padding: 0; }
  html, body { width: 1200px; height: 1021px; overflow: hidden; }
  body {
    background: var(--page-bg);
    font-family: "Open Sans", Arial, sans-serif;
    position: relative;
  }
  .card {
    position: absolute;
    width: 760px;
    height: 434px;
    box-shadow: 0 14px 30px rgba(0,0,0,0.25);
  }
  .card--back { left: 250px; top: 48px; background: var(--card-dark); }
  .card--front { left: 190px; top: 530px; background: var(--card-light); }

  .brand {
    position: absolute;
    left: 0; right: 0;
    display: flex;
    align-items: center;
    justify-content: center;
    gap: 18px;
  }
  .brand__dot {
    width: 46px; height: 46px;
    border-radius: 50%;
    background: var(--brand-blue);
  }
  .brand__name {
    font-weight: 700;
    font-size: 46px;
    letter-spacing: 1px;
    text-transform: uppercase;
    color: var(--brand-blue);
  }
  .card--back .brand { top: 184px; }
  .card--front .brand { top: 92px; }

  .details {
    position: absolute;
    left: 0; right: 0; top: 248px;
    display: flex;
    justify-content: center;
    align-items: stretch;
  }
  .person {
    text-align: right;
    padding-right: 26px;
    border-right: 1.5px solid var(--rule-grey);
  }
  .person__name {
    font-weight: 700;
    font-size: 27px;
    color: var(--brand-blue);
    text-transform: uppercase;
    letter-spacing: 0.5px;
  }
  .person__role {
    font-size: 21px;
    line-height: 1.2;
    color: var(--text-grey);
  }
  .contact {
    list-style: none;
    padding-left: 26px;
    padding-top: 18px;
    font-size: 21px;
    line-height: 1.3;
    color: var(--text-grey);
  }
  .contact li { display: flex; align-items: center; gap: 10px; }
  .contact svg { width: 17px; height: 17px; fill: var(--brand-blue); flex: none; }
  .contact__region { color: var(--brand-blue); }
</style>
</head>
<body>
  <section class="card card--back" aria-label="Business card back">
    <div class="brand">
      <span class="brand__dot"></span>
      <span class="brand__name">Marlo Vitality</span>
    </div>
  </section>

  <section class="card card--front" aria-label="Business card front">
    <div class="brand">
      <span class="brand__dot"></span>
      <span class="brand__name">Marlo Vitality</span>
    </div>
    <div class="details">
      <div class="person">
        <p class="person__name">Tomás Arribal</p>
        <p class="person__role">Wellness Coach<br>Consultant &amp; Trainer</p>
      </div>
      <ul class="contact">
        <li>
          <svg viewBox="0 0 24 24" aria-hidden="true"><path d="M6.6 10.8a15.1 15.1 0 0 0 6.6 6.6l2.2-2.2a1 1 0 0 1 1-.25 11.4 11.4 0 0 0 3.6.57 1 1 0 0 1 1 1V20a1 1 0 0 1-1 1A17 17 0 0 1 3 4a1 1 0 0 1 1-1h3.5a1 1 0 0 1 1 1c0 1.25.2 2.45.57 3.57a1 1 0 0 1-.25 1z"/></svg>
          <span>(+34) 612 480 397 <span class="contact__region">Spain</span></span>
        </li>
        <li>
          <svg viewBox="0 0 24 24" aria-hidden="true"><path d="M6.6 10.8a15.1 15.1 0 0 0 6.6 6.6l2.2-2.2a1 1 0 0 1 1-.25 11.4 11.4 0 0 0 3.6.57 1 1 0 0 1 1 1V20a1 1 0 0 1-1 1A17 17 0 0 1 3 4a1 1 0 0 1 1-1h3.5a1 1 0 0 1 1 1c0 1.25.2 2.45.57 3.57a1 1 0 0 1-.25 1z"/></svg>
          <span>+1 (555) 318 2046 <span class="contact__region">USA</span></span>
        </li>
        <li>
          <svg viewBox="0 0 24 24" aria-hidden="true"><path d="M12 2a10 10 0 1 0 0 20 10 10 0 0 0 0-20zm6.9 6h-3a15.6 15.6 0 0 0-1.4-3.6A8 8 0 0 1 18.9 8zM12 4c.8 1.2 1.5 2.5 1.9 4h-3.8c.4-1.5 1.1-2.8 1.9-4zM4.3 14a8 8 0 0 1 0-4h3.4a16 16 0 0 0 0 4zm.8 2h3a15.6 15.6 0 0 0 1.4 3.6A8 8 0 0 1 5.1 16zm3-8h-3a8 8 0 0 1 4.4-3.6A15.6 15.6 0 0 0 8.1 8zM12 20c-.8-1.2-1.5-2.5-1.9-4h3.8c-.4 1.5-1.1 2.8-1.9 4zm2.3-6H9.7a14.6 14.6 0 0 1 0-4h4.6a14.6 14.6 0 0 1 0 4zm.2 5.6a15.6 15.6 0 0 0 1.4-3.6h3a8 8 0 0 1-4.4 3.6zm1.8-5.6a16 16 0 0 0 0-4h3.4a8 8 0 0 1 0 4z"/></svg>
          <span>www.marlovitality.example</span>
        </li>
      </ul>
    </div>
  </section>
</body>
</html>
```